Lena Corvel Business Card

I need a business card that reflects my current website: itslenacorvel.com and screenshot attached. If we keep the color scheme of the site and sample card below that would be ideal. The business card should include the information on the attached sample cards.

Industry/Entity Type

Business

```html
<!DOCTYPE html>
<html lang="en">
<head>
<meta charset="utf-8">
<title>Lena Corvel Business Card</title>
<link rel="stylesheet" href="https://fonts.googleapis.com/css2?family=Lato:wght@400;700;900&display=swap">
<style>
  :root {
    --backdrop: #3b332e;
    --card: #1c1c1d;
    --card-edge: #111112;
    --mark-grey: #8a8a8c;
    --mark-dark: #2d2d2f;
    --teal: #1fc1c3;
    --text-light: #e4e4e4;
    --text-soft: #b9b9bb;
    --divider: #3a3a3c;
  }
  * { box-sizing: border-box; margin: 0; padding: 0; }
  html, body {
    width: 1200px; height: 827px; overflow: hidden;
    background: var(--backdrop);
    font-family: "Lato", Arial, sans-serif;
  }
  .canvas {
    width: 1200px; height: 827px;
    display: flex; align-items: center; justify-content: center; gap: 40px;
  }
  .card {
    width: 540px; height: 309px;
    background: radial-gradient(ellipse at 40% 30%, #252526 0%, var(--card) 60%, var(--card-edge) 100%);
    border-radius: 3px;
    box-shadow: 0 8px 24px rgba(0,0,0,.45);
    position: relative;
  }
  .card-front {
    display: flex; align-items: center; justify-content: center;
  }
  .wordmark {
    font-weight: 700;
    color: var(--mark-grey);
    letter-spacing: .02em;
  }
  .card-front .wordmark { font-size: 54px; }
  .card-back {
    display: flex; align-items: center; padding: 0 26px 0 30px;
  }
  .card-back .wordmark { font-size: 26px; width: 170px; }
  .divider {
    width: 1px; height: 140px; background: var(--divider); margin: 0 18px 0 10px;
  }
  .details { flex: 1; }
  .person-name {
    color: var(--teal); font-weight: 900; font-size: 20px; letter-spacing: .01em;
  }
  .person-role {
    color: var(--text-light); font-weight: 700; font-size: 11.5px; margin: 3px 0 12px;
  }
  .contact-list { list-style: none; }
  .contact-list li {
    display: flex; align-items: center; gap: 10px;
    color: var(--text-soft); font-size: 14px; line-height: 20px;
  }
  .contact-list svg { width: 14px; height: 14px; flex: none; }
  .social {
    display: flex; align-items: center; gap: 10px; margin-top: 12px;
    color: var(--text-light); font-size: 14px;
  }
  .social-square { width: 14px; height: 14px; background: var(--teal); border-radius: 2px; }
</style>
</head>
<body>
<main class="canvas">
  <section class="card card-front" aria-label="Card front">
    <span class="wordmark">Lena Corvel</span>
  </section>

  <section class="card card-back" aria-label="Card back">
    <span class="wordmark">Lena Corvel</span>
    <div class="divider"></div>
    <div class="details">
      <h1 class="person-name">LENA CORVEL AUBRIN</h1>
      <p class="person-role">Brand Curator/Digital StoryTeller/Social Entrepreneur</p>
      <ul class="contact-list">
        <li>
          <svg viewBox="0 0 14 14" aria-hidden="true"><path fill="var(--teal)" d="M3 1h3l1 3-2 1.5a8 8 0 0 0 3.5 3.5L10 7l3 1v3a2 2 0 0 1-2 2A10 10 0 0 1 1 3a2 2 0 0 1 2-2z"/></svg>
          555.014.2290
        </li>
        <li>
          <svg viewBox="0 0 14 14" aria-hidden="true"><rect x="1" y="3" width="12" height="8" fill="var(--teal)"/><path d="M1 3l6 5 6-5" fill="none" stroke="var(--card)" stroke-width="1.2"/></svg>
          me@itslenacorvel.com
        </li>
        <li>
          <svg viewBox="0 0 14 14" aria-hidden="true"><rect x="1.5" y="2.5" width="11" height="8" fill="none" stroke="var(--teal)" stroke-width="1.5"/><rect x="5" y="11" width="4" height="1.5" fill="var(--teal)"/></svg>
          www.itslenacorvel.com
        </li>
      </ul>
      <div class="social">
        <span class="social-square" aria-hidden="true"></span>
        @itslenacorvel
      </div>
    </div>
  </section>
</main>
</body>
</html>
```